Brindle Structures Construction Company Seeking Modern Website

We are a small construction company wanting to create a web presence. We don't have much in the way of current content but will get photos as they come in. Attached is a picture of our business card.
The pages we would like on the menu are:
Home
Portfolio
Product Specs
Testimonials
Our Process
Contact
Some designs we like are:
http://www.tovenquarnsheds.example/
http://www.qzrsheds.example/
http://pannowsheds.example/
http://wistenhalls.example/
Not much requirements other than that so feel free to be creative!
Updates
Target Market(s)
Construction
Commercial and Residential Buildings
Industry/Entity Type
Construction Company
Number of Pages Required
5+ page
Look and feel

```html
<!DOCTYPE html>
<html lang="en">
<head>
<meta charset="utf-8">
<title>Brindle Structures</title>
<link href="https://fonts.googleapis.com/css2?family=Montserrat:wght@500;700&family=Open+Sans:wght@400;600&family=Arimo:wght@400;700&display=swap" rel="stylesheet">
<style>
:root{
  --red:#d9231d;
  --red-dark:#b8140f;
  --red-light:#ee3a2f;
  --blue:#1a8fd0;
  --ink:#2b2b2b;
  --body:#6a6a6a;
  --band:#f2f2f2;
  --foot-top:#d8d8d8;
  --foot-bot:#efefef;
  --white:#ffffff;
}
*{margin:0;padding:0;box-sizing:border-box}
html,body{width:861px;height:1200px;overflow:hidden;background:var(--white)}
body{position:relative;font-family:"Arimo",Arial,sans-serif;color:var(--ink)}
.abs{position:absolute}

/* header */
.brand{left:72px;top:26px;font-family:"Montserrat",sans-serif;font-weight:700;font-size:26px;color:var(--blue);letter-spacing:-.3px}
.phone{left:580px;top:52px;display:flex;align-items:center;gap:4px;font-size:15px;color:#444;font-family:"Arimo",sans-serif}
.social{top:50px;width:22px;height:22px;border:1.5px solid #888;border-radius:50%}

/* nav */
.nav{left:0;top:94px;width:861px;height:37px;background:linear-gradient(#e4342b,#c0150f)}
.nav a{position:absolute;top:0;height:37px;line-height:37px;font-size:10.5px;font-weight:700;color:var(--white);text-decoration:none;transform:translateX(-50%)}
.nav .active{left:72px;width:64px;transform:none;text-align:center;background:var(--red-light)}

/* hero */
.hero{left:0;top:131px;width:861px;height:408px;background:linear-gradient(180deg,#f6a623 0%,#f4b53a 40%,#b8641a 62%,#1a1209 78%,#050403 100%)}

/* feature band */
.band{left:0;top:539px;width:861px;height:224px;background:var(--band)}
.card{top:576px;width:225px;height:152px;box-shadow:0 6px 8px -4px rgba(0,0,0,.35)}
.card-photo{position:absolute;inset:0}
.card-title{position:absolute;left:10px;font-family:"Montserrat",sans-serif;font-weight:700;font-size:15px;color:var(--white);letter-spacing:.2px}
.card-title::after{content:"";display:block;width:70px;height:2px;background:var(--red);margin-top:2px}
.card-overlay{position:absolute;inset:0;background:rgba(30,36,44,.72)}
.card-text{position:absolute;left:12px;top:48px;width:206px;font-size:8.6px;line-height:17px;font-weight:700;color:var(--white)}
.card-rule{position:absolute;left:10px;top:37px;width:205px;height:1px;background:#aaa}

/* welcome */
.welcome-title{left:73px;top:796px;font-family:"Open Sans",sans-serif;font-size:16px;color:var(--ink)}
.welcome-title span{color:var(--red);font-weight:600}
.welcome-copy{left:73px;top:825px;width:405px;font-size:9.2px;line-height:15.8px;color:var(--body)}
.read-more{left:73px;top:927px;font-size:9.5px;color:var(--red)}
.video{left:514px;top:798px;width:271px;height:163px;border-radius:14px;background:linear-gradient(135deg,#8a7a62,#5a6f86 55%,#7a6a55)}

/* footer */
.footer{left:0;top:1002px;width:861px;height:198px;background:linear-gradient(var(--foot-top),var(--foot-bot))}
.foot-head{top:1028px;font-family:"Montserrat",sans-serif;font-weight:500;font-size:11.5px;color:var(--red);letter-spacing:.3px}
.links{left:75px;top:1050px;list-style:none;font-size:8.6px;line-height:16.4px;color:#222}
.follow{left:219px;display:flex;align-items:center;gap:10px;font-size:10px;color:#222}
.follow i{display:block;width:21px;height:21px;border-radius:50%;background:#2a7fc1;border:2px solid #fff;box-shadow:0 1px 2px rgba(0,0,0,.3)}
.contact{left:375px;top:1050px;width:200px;font-size:8.6px;line-height:16.6px;color:#222}
.sub-note{right:76px;top:1050px;width:170px;text-align:right;font-size:8.6px;line-height:12.5px;color:#333}
.sub-field{left:616px;top:1080px;width:150px;height:27px;background:var(--white);border:1px solid #bbb}
.sub-go{left:765px;top:1080px;width:22px;height:27px;background:var(--red)}
.radio{top:1111px;display:flex;align-items:center;gap:6px;font-size:8.6px;color:#333}
.radio i{display:block;width:12px;height:12px;border:1px solid #555;border-radius:50%;background:#fff;position:relative}
.radio i.on::after{content:"";position:absolute;left:3px;top:3px;width:4px;height:4px;border-radius:50%;background:#222}
.divider{left:72px;top:1166px;width:713px;border-top:1px dashed #b5b5b5}
.copyright{left:0;top:1176px;width:861px;text-align:center;font-size:8.6px;color:#333}
.base-line{left:0;top:1196px;width:861px;height:4px;background:var(--red)}
</style>
</head>
<body>

<header>
  <div class="abs brand">Brindle Structures</div>
  <div class="abs phone">
    <svg width="13" height="16" viewBox="0 0 13 16"><path d="M3 1 L6 4 L4.5 6 C5.5 8.5 7 10 9 11 L11 9.5 L13 12.5 L11 15 C6 14 1.5 9 1 3 Z" fill="var(--red)"/></svg>
    99 30418852
  </div>
  <div class="abs social" style="left:707px"></div>
  <div class="abs social" style="left:736px"></div>
  <div class="abs social" style="left:765px"></div>
</header>

<nav class="abs nav">
  <a class="active" href="#">Home</a>
  <a style="left:177px" href="#">Portfolio</a>
  <a style="left:271px" href="#">Product Specs</a>
  <a style="left:375px" href="#">Testimonials</a>
  <a style="left:475px" href="#">Our Process</a>
  <a style="left:563px" href="#">Contact</a>
</nav>

<div class="abs hero" role="img" aria-label="Silhouetted construction workers on a building site at sunset with cranes"></div>

<section class="abs band"></section>

<div class="abs card" style="left:72px">
  <div class="card-photo" role="img" aria-label="Worker in hard hat at a building site" style="background:linear-gradient(135deg,#5d6b7a,#8a7448)"></div>
  <div class="card-overlay"></div>
  <div class="card-title" style="top:12px">WHAT WE DO</div>
  <div class="card-rule"></div>
  <p class="card-text">Lorem ipsum dolor sit amet, consectetur adipi-scing elit, sed do eiusmod tempor incididunt ut labore et dolore magna aliqua. Ut enim ad minim veniam, quis nostrud exercitation ullam-co laboris nisi ut aliquip .</p>
</div>

<div class="abs card" style="left:320px">
  <div class="card-photo" role="img" aria-label="Two engineers in hard hats reviewing plans on site" style="background:linear-gradient(135deg,#9aa6b0,#6f7f5a 60%,#b8b04a)"></div>
  <div class="card-title" style="top:120px">HISTORY</div>
</div>

<div class="abs card" style="left:565px">
  <div class="card-photo" role="img" aria-label="Yellow hard hat on a laptop with rolled blueprints" style="background:linear-gradient(135deg,#a8aeb4,#d6b52a 45%,#5a5f66)"></div>
  <div class="card-title" style="top:120px">MISSION STATEMENT</div>
</div>

<section>
  <h1 class="abs welcome-title" style="font-weight:400">Welcome To <span>Brindle Structures</span></h1>
  <p class="abs welcome-copy">Lorem ipsum dolor sit amet, consectetur adipiscing elit, sed do eiusmod tempor incididunt ut labore et dolore magna aliqua. Ut enim ad minim veniam, quis nostrud exercitation ullamco laboris nisi ut aliquip ex ea commodo consequat. Duis aute irure dolor in reprehenderit in voluptate velit esse cillum dolore eu fugiat nulla pariatur Sed ut perspiciatis unde omnis iste natus error sit voluptatem accusantium doloremque laudantium. sed quia non numquam eius modi tempora incidunt ut labore et dolore magnam.</p>
  <a class="abs read-more">Read More &#187;</a>
  <div class="abs video" role="img" aria-label="Video still of two builders in hard hats working on a frame"></div>
  <svg class="abs" style="left:631px;top:852px" width="48" height="48" viewBox="0 0 48 48" aria-hidden="true">
    <circle cx="24" cy="24" r="23" fill="var(--red)" stroke="#fff" stroke-opacity=".5" stroke-width="1.5"/>
    <path d="M18 13 L35 24 L18 35 Z" fill="#fff"/>
  </svg>
</section>

<footer>
  <div class="abs footer"></div>

  <h2 class="abs foot-head" style="left:72px">QUICK LINKS</h2>
  <ul class="abs links">
    <li>Home</li><li>Portfolio</li><li>Product Specs</li><li>Testimonials</li><li>Our Process</li><li>Contact</li>
  </ul>

  <h2 class="abs foot-head" style="left:217px">FOLLOW US</h2>
  <div class="abs follow" style="top:1058px"><i></i>Chatterline</div>
  <div class="abs follow" style="top:1090px"><i style="background:#3b5a9a"></i>Friendwall</div>
  <div class="abs follow" style="top:1123px"><i></i>Linkwork</div>

  <h2 class="abs foot-head" style="left:374px">CONTACT DETAILS</h2>
  <p class="abs contact">14 MARROW LANE, HESKETH TRADE PARK , HESKETH, WESTSHIRE<br>+44(0)1632960418<br>info@brindlestructures.example</p>

  <h2 class="abs foot-head" style="right:76px">SUBSCRIBE TO NEWSLETTER</h2>
  <p class="abs sub-note">Drop your email address below to receive Coupons &amp; Promos</p>
  <div class="abs sub-field"></div>
  <div class="abs sub-go">
    <svg width="22" height="27" viewBox="0 0 22 27"><path d="M8 7 L14 13.5 L8 20" fill="none" stroke="#fff" stroke-width="2.5"/></svg>
  </div>
  <div class="abs radio" style="left:646px"><i class="on"></i>Subscribe</div>
  <div class="abs radio" style="left:720px"><i></i>UnSubscribe</div>

  <div class="abs divider"></div>
  <p class="abs copyright">Copyright © 2013.All right reserved</p>
  <div class="abs base-line"></div>
</footer>

</body>
</html>
```